Business card design needed

I have started a new business called Marlow Auto Electrical, although the words Marlow Auto Electrical will be used on signage and documents I actually want to market the business as MAE. The services I offer are Mobile Auto Electrical, Automotive Air Conditioning and Test And Tag. My business will be targetting the Mining Industry, Civil, Rail, Agricultural and Workshop Testing And Tagging. My auto electrical service ranges from fault finding to new vehicle and mine compliance fit outs. I have a very strong focus on quality workmanship. I will upload the logo I have designed and want to use I am happy for the logo colour to change but the design itself must stay the same. I want the design to have a modern, eye catching, energetic feel. As I am a passionate motorsport fan I am happy for this to also influence the design. I am happy for the front of the card to have only the emblem and logo design and the back to have all the info.

Industry/Entity Type

Electrical

Contact Information for Business Card

MAE Marlow Auto Electrical, Dale Penrick, Auto Electrician, Mobile No 0417263859

Requirements
Must have
• On the business card it is mandatory that the following license numbers are shown:

MVRL38462
VDA L071348
ABN 61 839 204 518

```html
<!DOCTYPE html>
<html lang="en">
<head>
<meta charset="utf-8">
<title>Marlow Auto Electrical – Business Card</title>
<link rel="stylesheet" href="https://fonts.googleapis.com/css2?family=Montserrat:wght@500;600;700;800&display=swap">
<style>
  :root {
    --stage: #4a4538;
    --card: #ffffff;
    --card-shade: #e6e6e6;
    --yellow: #f6c623;
    --yellow-light: #f9d64f;
    --yellow-deep: #e2a92a;
    --name-yellow: #f2c02a;
    --ink: #141414;
    --white: #ffffff;
  }
  * { margin: 0; padding: 0; box-sizing: border-box; }
  html, body { width: 1200px; height: 1000px; overflow: hidden; }
  body {
    background: var(--stage);
    font-family: "Montserrat", Arial, sans-serif;
    position: relative;
  }
  .card {
    position: absolute;
    left: 314px;
    width: 593px;
    height: 365px;
    background: radial-gradient(ellipse at 50% 45%, var(--card) 55%, var(--card-shade) 100%);
    overflow: hidden;
  }
  .card--front { top: 110px; }
  .card--back { top: 516px; }
  .card__band { position: absolute; inset: 0; width: 100%; height: 100%; }

  .front__wordmark {
    position: absolute;
    left: 0; right: 0;
    top: 62px;
    text-align: center;
    font-weight: 800;
    font-size: 150px;
    line-height: 1;
    letter-spacing: -4px;
    color: var(--yellow);
  }
  .front__company {
    position: absolute;
    left: 0; right: 0;
    top: 242px;
    text-align: center;
    font-weight: 700;
    font-size: 26px;
    letter-spacing: -0.5px;
    color: var(--ink);
  }

  .back__name {
    position: absolute;
    left: 48px; top: 42px;
    font-weight: 700;
    font-size: 41px;
    letter-spacing: -0.5px;
    color: var(--name-yellow);
    text-transform: uppercase;
  }
  .back__role {
    position: absolute;
    left: 49px; top: 94px;
    font-weight: 600;
    font-size: 30px;
    letter-spacing: -0.5px;
    color: var(--ink);
  }
  .back__phone {
    position: absolute;
    left: 48px; top: 160px;
    display: flex;
    align-items: center;
    gap: 14px;
    font-weight: 700;
    font-size: 33px;
    letter-spacing: -1px;
    color: var(--ink);
  }
  .back__licences {
    position: absolute;
    left: 49px; top: 278px;
    list-style: none;
    font-weight: 700;
    font-size: 13.5px;
    line-height: 24px;
    color: var(--ink);
  }
  .back__wordmark {
    position: absolute;
    right: 30px; top: 236px;
    width: 200px;
    text-align: center;
    font-weight: 800;
    font-size: 78px;
    line-height: 1;
    letter-spacing: -2px;
    color: var(--white);
  }
  .back__company {
    position: absolute;
    right: 24px; top: 327px;
    font-weight: 700;
    font-size: 13.5px;
    letter-spacing: -0.2px;
    color: var(--ink);
  }
</style>
</head>
<body>

<section class="card card--front" aria-label="Card front">
  <svg class="card__band" viewBox="0 0 593 365" preserveAspectRatio="none" aria-hidden="true">
    <defs>
      <linearGradient id="front-band" x1="0" y1="0" x2="1" y2="1">
        <stop offset="0" stop-color="var(--yellow-light)"/>
        <stop offset="0.7" stop-color="var(--yellow)"/>
        <stop offset="1" stop-color="var(--yellow-deep)"/>
      </linearGradient>
    </defs>
    <polygon points="0,300 593,285 593,365 0,365" fill="url(#front-band)"/>
    <polygon points="0,300 120,318 593,365 0,365" fill="var(--yellow-light)" opacity="0.55"/>
  </svg>
  <div class="front__wordmark">MAE</div>
  <div class="front__company">MARLOW AUTO ELECTRICAL</div>
</section>

<section class="card card--back" aria-label="Card back">
  <svg class="card__band" viewBox="0 0 593 365" preserveAspectRatio="none" aria-hidden="true">
    <defs>
      <linearGradient id="back-band" x1="0" y1="0" x2="1" y2="1">
        <stop offset="0" stop-color="var(--yellow-light)"/>
        <stop offset="0.7" stop-color="var(--yellow)"/>
        <stop offset="1" stop-color="var(--yellow-deep)"/>
      </linearGradient>
    </defs>
    <polygon points="0,269 593,199 593,365 0,365" fill="url(#back-band)"/>
  </svg>

  <h1 class="back__name">Dale Penrick</h1>
  <p class="back__role">Auto Electrician</p>
  <p class="back__phone">
    <svg width="20" height="34" viewBox="0 0 20 34" aria-hidden="true">
      <rect x="2" y="2" width="16" height="30" rx="2" fill="none" stroke="var(--name-yellow)" stroke-width="3"/>
      <rect x="8" y="26" width="4" height="2" fill="var(--name-yellow)"/>
    </svg>
    <span>0417 263 859</span>
  </p>

  <ul class="back__licences">
    <li>MVRL38462</li>
    <li>VDA L071348</li>
    <li>ABN 61 839 204 518</li>
  </ul>

  <div class="back__wordmark">MAE</div>
  <div class="back__company">MARLOW AUTO ELECTRICAL</div>
</section>

</body>
</html>
```